Create the ONLY Supplement line for Male Entrepreneurs! (Veltro Prime MD)

I need a label designed for a new supplement brand that I am launching.

There are five products so need a design that I can simply change the wording for each individual product

The brand name is called veltro prime MD. The focus is male entrepreneurial health.

Target audience is men 35 to 55.

Concepts: the healthier you are in body the more money you will make in business.

Concept to copy: I want to make a clean minimalistic label mimicking Dallamore MD (google it and you'll see what I mean)

Target Market(s)

male entrepreneurs 35-55

Industry/Entity Type

Health Supplement

Colors

Designer to choose colors to be used in the design.

Requirements
Must have
• Modern classy design, similar to Dallamore MD.
Nice to have
• Highlight that the supplement is Doctor Approved.
Should not have
• No loud colors. Present it as high class.

```html
<!DOCTYPE html>
<html lang="en">
<head>
<meta charset="utf-8">
<title>Veltro Prime MD – Omega 3 Label</title>
<link href="https://fonts.googleapis.com/css2?family=Montserrat:wght@400;500;600;700&display=swap" rel="stylesheet">
<style>
  :root {
    --bg: #e3e5ea;
    --label-white: #f4f5f7;
    --band-grey-light: #c9cacd;
    --band-grey-dark: #aeb0b4;
    --ink: #4f5052;
    --ink-soft: #6a6b6e;
    --pill: #4a4b4d;
    --pill-text: #ffffff;
    --seal: #6e6f72;
  }
  * { margin: 0; padding: 0; box-sizing: border-box; }
  html, body {
    width: 1200px; height: 1200px; overflow: hidden;
    background: var(--bg);
    font-family: "Montserrat", sans-serif;
  }
  .label {
    position: absolute;
    left: 220px; top: 160px;
    width: 760px; height: 880px;
    background: var(--label-white);
    overflow: hidden;
    box-shadow: 0 10px 30px rgba(0,0,0,0.08);
  }
  .label__band {
    position: absolute; inset: 0;
    width: 100%; height: 100%;
  }
  .brand {
    position: absolute;
    left: 44px; top: 168px;
    display: flex; align-items: center; gap: 16px;
  }
  .brand__dot {
    width: 56px; height: 56px; border-radius: 50%;
    border: 3px solid var(--ink-soft);
  }
  .brand__name {
    font-weight: 500;
    font-size: 38px;
    letter-spacing: 0.02em;
    color: var(--ink-soft);
    text-transform: uppercase;
  }
  .product {
    position: absolute;
    left: 44px; top: 590px;
  }
  .product__name {
    font-weight: 700;
    font-size: 68px;
    color: var(--ink);
    line-height: 1;
  }
  .product__type {
    margin-top: 22px;
    font-weight: 500;
    font-size: 30px;
    color: var(--ink-soft);
  }
  .product__meta {
    position: absolute;
    left: 40px; top: 790px;
    display: flex; align-items: center; gap: 50px;
  }
  .count-pill {
    background: var(--pill);
    color: var(--pill-text);
    font-weight: 600;
    font-size: 26px;
    padding: 6px 16px;
    border-radius: 22px;
  }
  .seal {
    width: 100px; height: 100px; border-radius: 50%;
    background: var(--seal);
    margin-top: -10px;
  }
</style>
</head>
<body>
  <main class="label">
    <svg class="label__band" viewBox="0 0 760 880" preserveAspectRatio="none" aria-hidden="true">
      <defs>
        <linearGradient id="bandTone" x1="0" y1="0" x2="1" y2="1">
          <stop offset="0" stop-color="var(--band-grey-light)"/>
          <stop offset="1" stop-color="var(--band-grey-dark)"/>
        </linearGradient>
      </defs>
      <path d="M760 80 C560 210 260 500 0 620 L0 880 L760 880 Z" fill="url(#bandTone)"/>
    </svg>

    <div class="brand">
      <span class="brand__dot"></span>
      <span class="brand__name">Veltro Prime MD</span>
    </div>

    <section class="product">
      <h1 class="product__name">Omega 3</h1>
      <p class="product__type">Dietary Supplement</p>
    </section>

    <div class="product__meta">
      <span class="count-pill">90 Softgels</span>
      <span class="seal" role="img" aria-label="Doctor approved seal"></span>
    </div>
  </main>
</body>
</html>
```